I would like to start a new webpage for a dating site in switzerland.
The dating site is not a escort service at all and should not transmit any type of sexual connotation.
The is more a compagnionship dating : male pay to meet ladies for some time in which they invite them for dinner, coktail, museum visit or walking or even skying. the meeting will take place in big cities in switzerland: geneva, zurich, bern, lausannes.

```html
<!DOCTYPE html>
<html lang="en">
<head>
<meta charset="utf-8">
<title>Date Companion</title>
<link rel="stylesheet" href="https://fonts.googleapis.com/css2?family=Open+Sans:wght@400;600&family=Didact+Gothic&family=Signika:wght@400;600&display=swap">
<style>
:root{
  --pink:#e8185f;
  --blue:#1a7fa5;
  --ink:#444;
  --nav:#333;
  --muted:#7a7a7a;
  --panel:rgba(70,20,45,.45);
  --field:rgba(40,10,25,.55);
  --soft:#e9f3f8;
  --footer:#2a2a2a;
}
*{box-sizing:border-box;margin:0;padding:0}
html,body{width:833px;height:1200px;overflow:hidden;background:#fff}
body{position:relative;font-family:"Open Sans",Arial,sans-serif;color:var(--ink)}
.abs{position:absolute}
.top-rule{left:0;top:0;width:833px;height:5px;background:var(--pink)}
.account{left:673px;top:5px;display:flex;height:22px}
.account a{display:block;font-size:13px;line-height:22px;color:#fff;text-decoration:none;text-align:center}
.account .login{background:var(--pink);width:47px}
.account .signup{background:var(--blue);width:52px}
.brand{left:64px;top:46px;display:flex;align-items:center;gap:22px}
.brand-dot{width:56px;height:56px;border-radius:50%;background:var(--pink)}
.brand-name{font-size:39px;color:var(--ink);font-weight:400;letter-spacing:-.5px}
.nav{top:74px;left:497px}
.nav a{position:absolute;top:0;font-size:13px;color:var(--nav);text-decoration:none;white-space:nowrap}
.hero{left:0;top:125px;width:833px;height:440px;
  background:radial-gradient(ellipse at 50% 55%,#c9658f 0%,#9c3f6e 35%,#4b1e3a 75%,#2a1024 100%)}
.finder{left:284px;top:228px;width:316px;height:275px;background:var(--panel);border:1px solid rgba(255,255,255,.35)}
.finder h2{position:absolute;top:17px;left:0;width:100%;text-align:center;font-family:"Signika",sans-serif;font-weight:600;font-size:23px;color:#fff}
.label{position:absolute;left:20px;font-family:"Signika",sans-serif;font-size:13px;color:#fff}
.field{position:absolute;height:28px;background:var(--field);border:1px solid rgba(0,0,0,.5);font-family:"Signika",sans-serif;font-size:11px;color:#ececec;line-height:26px;padding-left:9px}
.field.select::after{content:"";position:absolute;right:10px;top:11px;border:5px solid transparent;border-top-color:#ddd}
.to{position:absolute;left:178px;top:116px;font-size:11px;color:#fff}
.search-btn{position:absolute;left:226px;top:235px;width:63px;height:26px;background:#3b3b3b;color:#fff;font-family:"Signika",sans-serif;font-size:13px;line-height:26px;text-align:center}
.results-title{left:0;top:598px;width:833px;text-align:center;font-family:"Didact Gothic",sans-serif;font-weight:400;font-size:26px;color:var(--pink)}
.profile-card{left:59px;top:658px;width:114px;height:138px;border:1px solid #a7d3e6;background:radial-gradient(circle at 50% 50%,#f0ece9 0%,#e3eef3 60%,#eaf5fa 100%);text-align:center}
.profile-card .name{margin-top:12px;font-size:13px;color:var(--blue);font-family:"Didact Gothic",sans-serif}
.profile-card hr{border:0;border-top:1px solid #c8c8c8;margin:5px 12px 6px}
.profile-card p{font-family:"Didact Gothic",sans-serif;font-size:12px;color:#666;line-height:22.5px}
.profile-card .share{display:flex;justify-content:center;gap:4px;margin-top:3px}
.profile-card .share span{width:16px;height:16px;border-radius:50%;background:#a9d6e8}
.member{width:150px;text-align:center;top:659px}
.member .photo{width:113px;height:113px;border-radius:50%;margin:0 auto;border:1px solid #ddd}
.member .name{margin-top:9px;font-family:"Didact Gothic",sans-serif;font-size:14px;color:#555}
.info{left:0;top:847px;width:833px;height:270px;background-color:var(--soft);
  background-image:radial-gradient(#cfe3ee 1px,transparent 1px);background-size:3px 3px}
.info h3{position:absolute;top:35px;font-family:"Didact Gothic",sans-serif;font-weight:400;color:var(--blue);white-space:nowrap}
.welcome h3{left:60px;font-size:26px}
.why h3{left:532px;font-size:22px;top:39px}
.copy{position:absolute;font-size:9px;line-height:17px;letter-spacing:-.3px;color:var(--muted)}
.welcome .copy{left:59px;width:445px;top:82px}
.welcome .copy p + p{margin-top:2px}
.why .copy{left:532px;width:255px;top:82px}
.register{position:absolute;left:59px;top:208px;width:110px;height:29px;background:#2f2f2f;border-radius:2px;color:#fff;font-family:"Signika",sans-serif;font-size:12px;line-height:29px;text-align:center}
.reasons{position:absolute;left:532px;top:143px;list-style:none}
.reasons li{font-size:11.5px;color:var(--pink);line-height:23.5px;padding-left:11px;position:relative}
.reasons li::before{content:"";position:absolute;left:0;top:9px;width:4px;height:4px;border-right:1px solid var(--pink);border-top:1px solid var(--pink);transform:rotate(45deg)}
.footer{left:0;top:1117px;width:833px;height:83px;background:var(--footer)}
.footer .links{position:absolute;left:60px;top:20px;font-family:Arial,sans-serif;font-size:10.5px;color:#fff}
.footer .legal{position:absolute;left:60px;top:46px;font-family:Arial,sans-serif;font-size:10.5px;color:#fff}
.social{position:absolute;top:29px;width:25px;height:25px}
</style>
</head>
<body>
<div class="abs top-rule"></div>
<div class="abs account"><a class="login" href="#">Login</a><a class="signup" href="#">Signup</a></div>

<div class="abs brand"><span class="brand-dot"></span><span class="brand-name">Date Companion</span></div>

<nav class="abs nav">
  <a href="#" style="left:0">HOME</a>
  <a href="#" style="left:59px">ABOUT US</a>
  <a href="#" style="left:142px">MEMBERS</a>
  <a href="#" style="left:221px">CONTACT</a>
</nav>

<div class="abs hero" role="img" aria-label="Photo of a smiling couple toasting with red wine at a candlelit dinner"></div>

<form class="abs finder">
  <h2>FIND YOUR COMPANION</h2>
  <span class="label" style="top:74px">Name:</span>
  <div class="field" style="left:66px;top:67px;width:223px">Enter your name</div>
  <span class="label" style="top:116px">Age:</span>
  <div class="field select" style="left:66px;top:109px;width:98px">Min Age</div>
  <span class="to">to</span>
  <div class="field select" style="left:189px;top:109px;width:100px">Max. Age</div>
  <span class="label" style="top:158px">Invite:</span>
  <div class="field select" style="left:66px;top:151px;width:223px">Dinner</div>
  <span class="label" style="top:203px">Place:</span>
  <div class="field select" style="left:66px;top:196px;width:223px">Zurich</div>
  <div class="search-btn">SEARCH</div>
</form>

<h2 class="abs results-title">SEARCH RESULTS</h2>

<div class="abs profile-card">
  <div class="name">ELENA</div>
  <hr>
  <p>Age: 27<br>Place: Zurich<br>Germany</p>
  <div class="share"><span></span><span></span></div>
</div>

<div class="abs member" style="left:191px">
  <div class="photo" role="img" aria-label="Portrait of a smiling woman with long dark hair" style="background:linear-gradient(160deg,#e6e2dc,#8a6a55 55%,#3b2a22)"></div>
  <div class="name">Anna Weber</div>
</div>
<div class="abs member" style="left:339px">
  <div class="photo" role="img" aria-label="Portrait of a woman in a denim jacket" style="background:linear-gradient(160deg,#c9b9a8,#8e6a55 50%,#3d4e68)"></div>
  <div class="name">Mira Sutter</div>
</div>
<div class="abs member" style="left:490px">
  <div class="photo" role="img" aria-label="Portrait of a dark-haired woman" style="background:linear-gradient(160deg,#3a3030,#9b7d74 55%,#5a4242)"></div>
  <div class="name">Anna Weber</div>
</div>
<div class="abs member" style="left:640px">
  <div class="photo" role="img" aria-label="Portrait of a woman with brown hair" style="background:linear-gradient(160deg,#f2eeea,#b08a6c 50%,#4a3426)"></div>
  <div class="name">Lea Perrin</div>
</div>

<section class="abs info">
  <div class="welcome">
    <h3>Welcome to Date Companion</h3>
    <div class="copy">
      <p>Claritas est etiam processus dynamicus, qui sequitur mutationem consuetudium lectorum. Mirum est notare quam littera gothica, quam nunc putamus parum claram, anteposuerit litterarum formas humanitatis per seacula quarta decima et quinta decima. Eodem modo typi, qui nunc nobis videntur parum clari, fiant sollemnes in futurum.</p>
      <p>Duis autem vel eum iriure dolor in hendrerit in vulputate velit esse molestie consequat, vel illum dolore eu feugiat nulla facilisis at vero eros et accumsan et iusto odio dignissim qui blandit praesent.</p>
    </div>
    <div class="register">Register For Free</div>
  </div>
  <div class="why">
    <h3>Why you choose us?</h3>
    <p class="copy">Ut wisi enim ad minim veniam, quis nostrud exerci tation ullamcorper suscipit lobortis nisl ut aliquip ex ea commodo consequat. Duis autem vel eum iriure dolor.</p>
    <ul class="reasons">
      <li>Phasellus felis dolor sceler</li>
      <li>Tempus eget lobortisro.</li>
      <li>Aliquam nec erat at purus</li>
      <li>Vestibulum ligula augue</li>
    </ul>
  </div>
</section>

<footer class="abs footer">
  <div class="links">Terms and Conditions | Privacy Promise | FAQ's | Contact Us</div>
  <div class="legal">Copyright © 2013. All Rights Reserved.</div>
  <span class="social" style="left:617px;background:#3b5998" aria-label="Social link"></span>
  <span class="social" style="left:651px;background:#2aa3d8" aria-label="Social link"></span>
  <span class="social" style="left:685px;background:#f26522" aria-label="Feed link"></span>
  <span class="social" style="left:719px;background:#e02a20" aria-label="Video link"></span>
</footer>
</body>
</html>
```